PWRPT design for Company

Project: Develop a pwrpt for QT7lx. This can be just a blank pwrpt with standard templates that we can use to build our content and solutions around.
Website: www.qt7lx.example
Color Pallet: Try to use the color schema from our website.
PWRPT Design Tips: While we are a research-based company, our primary target is schools and school districts. We say our work is RESEARCH, POLICY, AND PRACTICE. I would like images that represent “WHY” our research matters, i.e. students, teachers, and administrators. If you can use images and stock photos that represent students with diverse backgrounds, teachers that are diverse and clearly teaching, and administrators that run a school, university, etc. We are in the process of updating our website, but the color scheme will remain the same.
Additional Information:
We built, researched, and designed, www.brvk-tq.example .
We built, researched, and designed, http://87pxgamma.example/olav/index.html
Target Market(s)
EDUCATION
Industry/Entity Type
It Company

```html
<!DOCTYPE html>
<html lang="en">
<head>
<meta charset="utf-8">
<title>QT7lx Welcome Slide</title>
<link href="https://fonts.googleapis.com/css2?family=Raleway:wght@300;400;800&display=swap" rel="stylesheet">
<style>
  :root {
    --orange: #f47c20;
    --slate: #4d5659;
    --slate-stripe: #5c6366;
    --ink: #3a3f42;
    --white: #ffffff;
  }
  * { margin: 0; padding: 0; box-sizing: border-box; }
  html, body { width: 1200px; height: 900px; overflow: hidden; background: var(--white); }
  body { font-family: "Raleway", Arial, sans-serif; }

  .slide { position: relative; width: 1200px; height: 900px; overflow: hidden; background: var(--white); }

  .hero { position: absolute; left: 0; top: 0; width: 1200px; height: 735px; }
  .hero svg { display: block; }

  .hero-copy { position: absolute; left: 667px; top: 530px; color: var(--white); }
  .hero-title { font-weight: 800; font-size: 58px; letter-spacing: 1px; line-height: 1; }
  .hero-program { font-weight: 400; font-size: 37px; margin-top: 14px; line-height: 1.1; }
  .hero-date { font-weight: 300; font-size: 26px; margin-top: 16px; }

  .footer { position: absolute; left: 0; top: 735px; width: 1200px; height: 150px; }
  .legal { position: absolute; left: 40px; top: 56px; width: 660px; font-weight: 300; font-size: 16.5px; line-height: 1.5; color: var(--ink); }

  .brand { position: absolute; right: 45px; top: 34px; text-align: right; }
  .brand-name { display: block; font-weight: 400; font-size: 60px; line-height: 1; color: var(--ink); }
  .brand-tagline { margin-top: 16px; font-weight: 400; font-size: 14px; letter-spacing: 1.5px; color: var(--slate); }

  .base-bar { position: absolute; left: 0; top: 885px; width: 1200px; height: 15px; background: var(--slate); }
</style>
</head>
<body>
<main class="slide">
  <section class="hero">
    <svg width="1200" height="735" viewBox="0 0 1200 735">
      <defs>
        <linearGradient id="photoTone" x1="0" y1="0" x2="1" y2="1">
          <stop offset="0" stop-color="#9fb07a"/>
          <stop offset="0.35" stop-color="#c9a58c"/>
          <stop offset="0.7" stop-color="#7d4f52"/>
          <stop offset="1" stop-color="#3e4c63"/>
        </linearGradient>
      </defs>
      <rect class="hero-photo" x="0" y="0" width="900" height="735" fill="url(#photoTone)" role="img" aria-label="Photo of three diverse students reading a book together outdoors"/>
      <polygon class="hero-stripe" points="840,0 870,0 563,735 533,735" fill="var(--slate-stripe)"/>
      <polygon class="hero-panel" points="855,0 1200,0 1200,735 548,735" fill="var(--orange)"/>
    </svg>
    <div class="hero-copy">
      <h1 class="hero-title">WELCOME</h1>
      <p class="hero-program">Route4Futures (R4F)</p>
      <p class="hero-date">August 21st, 2017</p>
    </div>
  </section>

  <footer class="footer">
    <p class="legal">© 2017 All rights reserved. Contains confidential and proprietary information and may not be disclosed or reproduced without the prior written consent of QT7lx</p>
    <div class="brand">
      <span class="brand-name">QT7lx</span>
      <p class="brand-tagline">Research, Policy and Practice</p>
    </div>
  </footer>
  <div class="base-bar"></div>
</main>
</body>
</html>
```